tri-fold brochure design for psychology practice - all content provided

we are a psychology practice that specialises in diagnostic and educational assessments for children, adolescents and adults. We have an existing logo and I am attaching a word doc (tri-fold brochure) with the required content. I am also attaching our logo and other relevant content docs. The layout is only a sample and we are looking for someone to put this together into a consistent and better layout.

Target Market(s)

parents

Industry/Entity Type

education and health

Font styles to use
Other font styles liked:
• crimsonpro

Requirements
Must have
• our logo and the provided content

```html
<!DOCTYPE html>
<html lang="en">
<head>
<meta charset="utf-8">
<title>Sproutwell tri-fold brochure</title>
<link href="https://fonts.googleapis.com/css2?family=Crimson+Pro:wght@500;700&family=Montserrat:wght@400;600;700;800&display=swap" rel="stylesheet">
<style>
:root{
  --green:#6fb83f;
  --green-dark:#3f8a2f;
  --blue:#2a6c9c;
  --charcoal:#2e2f31;
  --slate:#44474a;
  --paper:#ececec;
  --paper-light:#f6f6f6;
  --ink:#3b3b3b;
  --muted:#6b6b6b;
  --white:#ffffff;
}
*{box-sizing:border-box;margin:0;padding:0}
html,body{width:900px;height:1200px;overflow:hidden;background:var(--white)}
body{position:relative;font-family:"Montserrat",Arial,sans-serif;color:var(--ink)}
.spread{position:absolute;left:20px;width:750px;height:570px;box-shadow:0 2px 8px rgba(0,0,0,.25);overflow:hidden}
.spread-front{top:20px}
.spread-inside{top:610px}
.panel{position:absolute;top:0;width:250px;height:570px;overflow:hidden}
.panel-1{left:0}.panel-2{left:250px}.panel-3{left:500px}
.side-label{position:absolute;left:805px;width:80px;font-family:"Crimson Pro",Georgia,serif;font-weight:500;font-size:30px;letter-spacing:2px;color:#111;writing-mode:vertical-rl;text-align:center}
.label-front{top:200px;height:200px}
.label-inside{top:790px;height:220px}
.photo{position:absolute;left:0;width:100%}
.body-text{font-size:7.4px;line-height:1.5;color:var(--ink)}

/* front panel 1 */
.front-left{background:linear-gradient(180deg,#e9e9e9,#d9d9d9)}
.front-left .photo{top:0;height:228px;background:linear-gradient(135deg,#f3d6c9,#e9b9a6 45%,#c7a07f)}
.stage{position:absolute;left:22px;width:206px;height:72px;border-radius:4px;padding:8px 10px;color:var(--white)}
.stage h3{font-size:9px;font-weight:800;letter-spacing:1px;margin-bottom:5px}
.stage p{font-size:6.8px;line-height:1.45}
.stage-green{background:linear-gradient(90deg,var(--green),#8cc960)}
.stage-blue{background:linear-gradient(90deg,var(--blue),#3f88bd)}
.stage-1{top:250px}.stage-2{top:352px}.stage-3{top:454px}
.stage-arrow{position:absolute;left:113px;width:0;height:0;border-left:12px solid transparent;border-right:12px solid transparent;border-top:14px solid var(--blue)}
.arrow-1{top:328px}.arrow-2{top:430px}

/* front panel 2 */
.front-back{background:linear-gradient(180deg,#f2f2f2,#dedede)}
.leaves{position:absolute;left:110px;top:-10px;width:300px;height:230px;border-radius:0 0 0 60%;background:radial-gradient(circle at 40% 45%,#7fc24a,#3e8b2c 60%,#2a6320)}
.brand{display:flex;align-items:center;justify-content:center;gap:7px;font-family:"Montserrat",Arial,sans-serif;font-weight:700;color:var(--charcoal)}
.brand-dot{border-radius:50%;background:var(--green)}
.brand-back{position:absolute;left:0;width:250px;top:360px;font-size:15px}
.brand-back .brand-dot{width:16px;height:16px}
.contact{position:absolute;left:42px;top:415px;list-style:none}
.contact li{display:flex;align-items:center;gap:9px;font-size:7.8px;color:var(--ink);margin-bottom:11px}
.contact svg{width:15px;height:15px;flex:none}

/* front panel 3 */
.cover{background:var(--paper-light)}
.cover-top{position:absolute;left:0;top:0;width:250px;height:230px;background:linear-gradient(160deg,#3a3c3f,#55585b)}
.cover-leaves{position:absolute;left:-30px;top:-10px;width:170px;height:160px;border-radius:0 0 70% 0;background:radial-gradient(circle at 40% 40%,#86c653,#3f8b2d 65%,#2b6521)}
.brand-cover{position:absolute;left:0;width:250px;top:255px;font-size:19px}
.brand-cover .brand-dot{width:22px;height:22px}
.taglines{position:absolute;left:0;width:250px;top:392px;text-align:center;font-family:"Montserrat",Arial,sans-serif;font-weight:700;font-size:13px;letter-spacing:1.5px;line-height:1.45;color:var(--charcoal)}
.wave{position:absolute;left:0;bottom:0;width:250px;height:80px}

/* inside panel 1 */
.inside-left{background:var(--paper)}
.inside-left .photo{top:0;height:215px;background:linear-gradient(135deg,#f4e1c2,#e7b66f 40%,#7fb2d6)}
.band-title{position:absolute;left:0;top:215px;width:250px;height:38px;background:linear-gradient(90deg,var(--green-dark),var(--green));color:var(--white);font-weight:800;font-size:16px;padding:9px 18px}
.inside-left .body-text{position:absolute;left:18px;top:268px;width:214px}
.body-text p{margin-bottom:8px}

/* inside panel 2 */
.inside-mid{background:linear-gradient(180deg,#e4eedb,#ececec 45%)}
.inside-mid .copy{position:absolute;left:18px;top:20px;width:214px}
.services{list-style:none;margin:4px 0 9px}
.services li{display:flex;align-items:center;gap:6px;margin-bottom:3px}
.services svg{width:8px;height:8px;flex:none}
.inside-mid .photo{top:380px;height:190px;background:linear-gradient(120deg,#e2483d,#f2b233 30%,#5db14b 60%,#3179c4)}

/* inside panel 3 */
.process{background:linear-gradient(180deg,var(--charcoal),var(--slate))}
.process h2{position:absolute;left:22px;top:24px;font-family:"Crimson Pro",Georgia,serif;font-weight:700;font-size:19px;letter-spacing:1.5px;color:var(--white)}
.process-rule{position:absolute;left:22px;top:52px;width:206px;height:2px;background:var(--green)}
.steps{position:absolute;left:22px;top:72px;width:212px;list-style:none}
.step{display:flex;gap:10px;margin-bottom:18px}
.step-num{flex:none;width:26px;height:26px;background:var(--green);color:var(--white);font-weight:800;font-size:13px;display:flex;align-items:center;justify-content:center;border-radius:3px}
.step p{font-size:7px;line-height:1.5;color:#e5e5e5;border-left:1px solid var(--green);padding-left:8px;min-height:64px}
</style>
</head>
<body>

<section class="spread spread-front">
  <div class="panel panel-1 front-left">
    <div class="photo" role="img" aria-label="Photograph of a mother and young daughter reading together"></div>
    <div class="stage stage-green stage-1">
      <h3>UNDERSTANDING</h3>
      <p>We take time to learn about each person, their story, strengths and the concerns that brought them to us.</p>
    </div>
    <div class="stage-arrow arrow-1"></div>
    <div class="stage stage-blue stage-2">
      <h3>IDENTIFYING</h3>
      <p>Careful, evidence-based assessment helps identify learning, developmental and emotional needs.</p>
    </div>
    <div class="stage-arrow arrow-2"></div>
    <div class="stage stage-green stage-3">
      <h3>GUIDING</h3>
      <p>Clear reports and practical advice guide families, schools and clients towards the right support.</p>
    </div>
  </div>

  <div class="panel panel-2 front-back">
    <div class="leaves" role="img" aria-label="Green monstera plant leaves"></div>
    <div class="brand brand-back"><span class="brand-dot"></span>Sproutwell</div>
    <ul class="contact">
      <li><svg viewBox="0 0 16 16"><path d="M8 1a5 5 0 0 0-5 5c0 4 5 9 5 9s5-5 5-9a5 5 0 0 0-5-5zm0 7a2 2 0 1 1 0-4 2 2 0 0 1 0 4z" fill="var(--green)"/></svg>12 Wattle Lane, Brookfield NSW 2150</li>
      <li><svg viewBox="0 0 16 16"><path d="M4 1l3 3-2 2a9 9 0 0 0 5 5l2-2 3 3-2 3C7 15 1 9 1 3z" fill="var(--green)"/></svg>02 5550 1234</li>
      <li><svg viewBox="0 0 16 16"><rect x="1" y="3" width="14" height="10" rx="1" fill="var(--green)"/><path d="M1 4l7 5 7-5" stroke="#fff" stroke-width="1.2" fill="none"/></svg>hello@sproutwell.example</li>
      <li><svg viewBox="0 0 16 16"><circle cx="8" cy="8" r="6.5" fill="none" stroke="var(--green)" stroke-width="1.5"/><path d="M1.5 8h13M8 1.5c-3 3-3 10 0 13M8 1.5c3 3 3 10 0 13" stroke="var(--green)" stroke-width="1.1" fill="none"/></svg>www.sproutwell.example</li>
    </ul>
  </div>

  <div class="panel panel-3 cover">
    <div class="cover-top"></div>
    <div class="cover-leaves" role="img" aria-label="Green monstera plant leaves"></div>
    <div class="brand brand-cover"><span class="brand-dot"></span>Sproutwell</div>
    <div class="taglines">UNDERSTANDING<br>IDENTIFYING<br>GUIDING</div>
    <svg class="wave" viewBox="0 0 250 80" preserveAspectRatio="none">
      <path d="M0 40 C70 10 160 70 250 25 L250 80 L0 80 Z" fill="var(--slate)"/>
      <path d="M0 55 C80 30 170 85 250 45 L250 80 L0 80 Z" fill="var(--green)"/>
    </svg>
  </div>
</section>

<section class="spread spread-inside">
  <div class="panel panel-1 inside-left">
    <div class="photo" role="img" aria-label="Photograph of a young child playing with colourful building blocks"></div>
    <div class="band-title">Who We Are</div>
    <div class="body-text">
      <p>Sproutwell is a team with a passion for helping people thrive. We are a team of psychologists and teachers who have experience in both educational and clinical settings.</p>
      <p>We understand the challenges parents face in working out what is best for their children, and are committed to being a place where every family feels heard and supported.</p>
      <p>We are passionate about working as a team with families to explain the diagnosis and assessment process clearly.</p>
      <p>We believe that quality and compassionate assessment leads to happier, healthier, more confident learners.</p>
    </div>
  </div>

  <div class="panel panel-2 inside-mid">
    <div class="copy body-text">
      <p>We work collaboratively with other professionals to ensure that your child, teen or adult receives the right diagnosis and the support needed to reach their full potential.</p>
      <p>We are qualified to give formal diagnoses for mental health conditions and specific learning disorders. This includes:</p>
      <ul class="services">
        <li><svg viewBox="0 0 10 10"><path d="M1 5l3 3 5-6" stroke="var(--green)" stroke-width="2" fill="none"/></svg>Attention Deficit Hyperactivity Disorder</li>
        <li><svg viewBox="0 0 10 10"><path d="M1 5l3 3 5-6" stroke="var(--green)" stroke-width="2" fill="none"/></svg>Autism Spectrum Disorder</li>
        <li><svg viewBox="0 0 10 10"><path d="M1 5l3 3 5-6" stroke="var(--green)" stroke-width="2" fill="none"/></svg>Specific Learning Disorders</li>
        <li><svg viewBox="0 0 10 10"><path d="M1 5l3 3 5-6" stroke="var(--green)" stroke-width="2" fill="none"/></svg>Language Disorders</li>
        <li><svg viewBox="0 0 10 10"><path d="M1 5l3 3 5-6" stroke="var(--green)" stroke-width="2" fill="none"/></svg>Anxiety Disorders</li>
        <li><svg viewBox="0 0 10 10"><path d="M1 5l3 3 5-6" stroke="var(--green)" stroke-width="2" fill="none"/></svg>Mood Disorders</li>
        <li><svg viewBox="0 0 10 10"><path d="M1 5l3 3 5-6" stroke="var(--green)" stroke-width="2" fill="none"/></svg>Giftedness</li>
      </ul>
      <p>We also provide school readiness assessments and cognitive testing to guide decisions about learning support and placement.</p>
    </div>
    <div class="photo" role="img" aria-label="Photograph of colourful crayons and pencils"></div>
  </div>

  <div class="panel panel-3 process">
    <h2>THE PROCESS</h2>
    <div class="process-rule"></div>
    <ol class="steps">
      <li class="step"><span class="step-num">1</span><p>An initial phone call to discuss your concerns and which assessment best suits your needs, followed by intake forms.</p></li>
      <li class="step"><span class="step-num">2</span><p>A parent or client interview to gather history, developmental information and goals for the assessment.</p></li>
      <li class="step"><span class="step-num">3</span><p>Assessment sessions with your psychologist, using standardised tests in a calm and friendly space.</p></li>
      <li class="step"><span class="step-num">4</span><p>A feedback session to explain results, discuss any diagnosis and talk through the next steps.</p></li>
      <li class="step"><span class="step-num">5</span><p>A clear written report with practical recommendations for home, school and other professionals.</p></li>
    </ol>
  </div>
</section>

<div class="side-label label-front">FRONT</div>
<div class="side-label label-inside">INSIDE</div>

</body>
</html>
```